Legal Postcard for Carlvista Film Works

LEGAL VIDEO SERVICES- Expert & Lay Witness Depositions- Day in the Life Videos- Security & Surveillance Video Editing- Onsite Video Documentation- Ability to make bad video clearer- Focus Groups & Video Monitoring- Video Conversion and Duplication- Over 15 Years of Legal Video Experience

Phone: 418.562.7391
Email: Walter@Carlvista.example

Target Market(s)

Law Firms

Industry/Entity Type

Legal

Font styles to use
Serif

Requirements
Must have
• The information in my description, my logo & picture.
• Nice design touches and accents
• Return address & Logo on mailing side of postcard, all other info on the main side
• Colors should be consistent with my logo

```html
<!DOCTYPE html>
<html lang="en">
<head>
<meta charset="utf-8">
<title>Carlvista Film Works – Legal Postcard</title>
<link rel="stylesheet" href="https://fonts.googleapis.com/css2?family=Cinzel:wght@600;700&family=Libre+Baskerville:wght@400;700&display=swap">
<style>
  :root {
    --page: #2b2b2b;
    --cream: #f7f1e6;
    --cream-deep: #e9dcc4;
    --brown: #6b2a14;
    --brown-dark: #4a1a0b;
    --rust: #a3462a;
    --gold: #c9a24c;
    --gold-light: #f0d894;
    --ink: #3a2a20;
    --red: #9c1c12;
    --grey: #8a8a8a;
  }
  * { margin: 0; padding: 0; box-sizing: border-box; }
  html, body { width: 900px; height: 1200px; overflow: hidden; }
  body {
    background: var(--page);
    font-family: "Libre Baskerville", Georgia, serif;
    color: var(--ink);
    position: relative;
  }
  .postcard {
    position: absolute;
    left: 100px;
    width: 700px;
    height: 500px;
    background: linear-gradient(160deg, #ffffff 0%, var(--cream) 60%, var(--cream-deep) 100%);
    overflow: hidden;
  }
  .postcard--front { top: 50px; }
  .postcard--back { top: 620px; }

  /* Front */
  .front-swoosh { position: absolute; inset: 0; }
  .brand-title {
    position: absolute; top: 22px; left: 300px; width: 380px;
    font-family: "Cinzel", "Times New Roman", serif;
    font-weight: 700; font-size: 40px; letter-spacing: 1px;
    color: var(--brown); text-align: center;
  }
  .title-rule {
    position: absolute; top: 78px; left: 300px; width: 380px; height: 2px;
    background: linear-gradient(90deg, transparent, var(--gold), transparent);
  }
  .studio-photo {
    position: absolute; top: 26px; left: 24px; width: 160px; height: 120px;
    border: 4px solid #fff; box-shadow: 0 2px 6px rgba(0,0,0,.35);
    background: linear-gradient(135deg, #1a1a1a, #5a1e1e 55%, #b83a2a);
  }
  .operator-photo {
    position: absolute; top: 92px; left: 352px; width: 300px; height: 300px;
    border-radius: 50%;
    background: radial-gradient(circle at 45% 40%, #f2e6d6 0%, #c98a62 45%, var(--brown) 80%);
    box-shadow: 0 4px 14px rgba(0,0,0,.3);
  }
  .service-plate {
    position: absolute; top: 170px; left: 24px; width: 250px; height: 62px;
    background: linear-gradient(180deg, var(--gold-light), var(--gold));
    border-left: 6px solid var(--brown);
    padding: 10px 16px;
    font-weight: 700; font-size: 17px; line-height: 1.2; color: var(--brown-dark);
  }
  .service-list {
    position: absolute; top: 248px; left: 30px; width: 300px; list-style: none;
    font-size: 12px; line-height: 1.6; color: var(--ink);
  }
  .service-list li::before {
    content: ""; display: inline-block; width: 7px; height: 7px; margin-right: 8px;
    border: 1.5px solid var(--brown); border-radius: 50%; vertical-align: 1px;
  }
  .service-note {
    position: absolute; top: 346px; left: 30px; width: 300px;
    font-weight: 700; font-size: 14px; line-height: 1.35; color: var(--red);
  }

  /* Back */
  .divider {
    position: absolute; top: 40px; left: 350px; width: 1px; height: 420px; background: #cfc4b2;
  }
  .sign-string { position: absolute; top: 0; left: 40px; }
  .sign-board {
    position: absolute; top: 120px; left: 50px; width: 240px; height: 150px;
    background: linear-gradient(180deg, var(--rust), var(--brown));
    border: 3px solid var(--brown-dark); border-radius: 4px;
    box-shadow: 0 4px 8px rgba(0,0,0,.35);
    padding: 14px 16px; color: #fff;
  }
  .sign-heading {
    font-size: 13px; font-weight: 700; padding-bottom: 6px; margin-bottom: 8px;
    border-bottom: 1px solid var(--gold-light);
  }
  .sign-list { list-style: none; font-size: 11.5px; line-height: 1.75; }
  .sign-list li::before {
    content: ""; display: inline-block; width: 6px; height: 6px; margin-right: 8px;
    border: 1.5px solid #fff; border-radius: 50%; vertical-align: 1px;
  }
  .return-address {
    position: absolute; top: 380px; left: 40px;
    font-size: 12.5px; font-weight: 700; line-height: 1.5; color: var(--brown-dark);
  }
  .stamp-box {
    position: absolute; top: 30px; left: 580px; width: 90px; height: 100px;
    border: 2px solid #333; background: #fff;
  }
  .back-brand {
    position: absolute; top: 205px; left: 420px; width: 240px; text-align: center;
  }
  .back-brand-mark {
    display: inline-block; width: 26px; height: 26px; border-radius: 50%;
    background: var(--grey); vertical-align: middle; margin-right: 10px;
  }
  .back-brand-name {
    font-size: 30px; font-weight: 700; color: var(--grey); vertical-align: middle;
  }
  .web-address {
    position: absolute; top: 270px; left: 380px; width: 300px; text-align: center;
    font-size: 11px; color: var(--grey);
  }
</style>
</head>
<body>

<section class="postcard postcard--front" aria-label="Postcard front">
  <svg class="front-swoosh" width="700" height="500" viewBox="0 0 700 500" aria-hidden="true">
    <defs>
      <linearGradient id="swooshGrad" x1="0" y1="0" x2="1" y2="0">
        <stop offset="0" stop-color="#e9dcc4"/>
        <stop offset="1" stop-color="#d8c3a0"/>
      </linearGradient>
    </defs>
    <path d="M0 430 C200 390 420 470 700 410 L700 500 L0 500 Z" fill="url(#swooshGrad)"/>
    <path d="M0 450 C220 410 430 490 700 430" fill="none" stroke="#c9a24c" stroke-width="2"/>
  </svg>

  <div class="studio-photo" role="img" aria-label="Photo of a videographer with a camera on a red-lit set"></div>
  <h1 class="brand-title">Carlvista</h1>
  <div class="title-rule"></div>
  <div class="operator-photo" role="img" aria-label="Photo of the videographer crouching with a video camera"></div>

  <div class="service-plate">LEGAL VIDEO<br>SERVICES</div>
  <ul class="service-list">
    <li>Expert &amp; Lay Witness Depositions</li>
    <li>Day in the Life Videos</li>
    <li>Security &amp; Surveillance Video Editing</li>
    <li>Onsite Video Documentation</li>
  </ul>
  <p class="service-note">Ability to make bad video clearer- Focus Groups &amp; Video Monitoring- Video Conversion and Duplication</p>
</section>

<section class="postcard postcard--back" aria-label="Postcard mailing side">
  <svg class="sign-string" width="260" height="130" viewBox="0 0 260 130" aria-hidden="true">
    <circle cx="130" cy="40" r="5" fill="#555"/>
    <path d="M130 40 L40 122 M130 40 L220 122" stroke="#555" stroke-width="2" fill="none"/>
  </svg>
  <div class="sign-board">
    <h2 class="sign-heading">Video Production Services</h2>
    <ul class="sign-list">
      <li>Legal Video Production</li>
      <li>Product Process</li>
      <li>Training &amp; Safety Videos</li>
      <li>Company Profile Video</li>
    </ul>
  </div>

  <address class="return-address" style="font-style:normal">
    Carlvista<br>
    Brookhaven, MN 55990<br>
    United States<br>
    ph: 418.562.7391<br>
    Walter@Carlvista.example
  </address>

  <div class="divider"></div>
  <div class="stamp-box" aria-label="Stamp area"></div>

  <div class="back-brand">
    <span class="back-brand-mark"></span><span class="back-brand-name">Carlvista</span>
  </div>
  <p class="web-address">www.Carlvista.example</p>
</section>

</body>
</html>
```